Business Card Design Project

Logo, Phone Number, slogan, must be included on front of card. Services must be listed: Lawn Service, Fertilization, Pool Service, Pressure Washing. and a space to "write in" salesmans name.
Slogan "Your Everything Outside Company"
Phone: 555-204-3816
Email: brightmeadowgroup@mailvane.com
Looking for a bold yet simple design to enforce brand recognition.

Target Market(s)

Middle to upper class US homeowners

Industry/Entity Type

Business

Requirements
Must have
• Logo, Phone, and Slogan on front
Should not have
• cluttered background

```html
<!DOCTYPE html>
<html lang="en">
<head>
<meta charset="utf-8">
<title>Brightmeadow Services – Business Card</title>
<link href="https://fonts.googleapis.com/css2?family=Gochi+Hand&family=Marcellus+SC&display=swap" rel="stylesheet">
<style>
  :root {
    --navy: #2b5d8e;
    --navy-deep: #244f7c;
    --sky: #2f8fc0;
    --green: #7ab648;
    --ink-blue: #2d5f93;
    --card-line: #dcdcdc;
    --paper: #ffffff;
    --light-text: #e9eff6;
  }
  * { margin: 0; padding: 0; box-sizing: border-box; }
  html, body {
    width: 1200px; height: 684px; overflow: hidden;
    background: var(--paper);
  }
  .canvas { position: relative; width: 1200px; height: 684px; }

  /* Front card */
  .card-front {
    position: absolute; left: 80px; top: 198px;
    width: 515px; height: 288px;
    background: var(--paper);
    border: 1px solid var(--card-line);
    overflow: hidden;
  }
  .edge-stripe { position: absolute; left: 0; width: 6px; }
  .edge-stripe--blue { top: 0; height: 94px; background: var(--navy); }
  .edge-stripe--green { top: 94px; bottom: 0; background: var(--green); }

  .brand-name {
    position: absolute; left: 57px; top: 68px;
    font-family: "Marcellus SC", serif;
    font-size: 27px; line-height: 30px;
    color: var(--navy);
    letter-spacing: 1px;
  }

  .slogan {
    position: absolute; left: 296px; top: 122px;
    font-family: "Gochi Hand", cursive;
    font-size: 22px; line-height: 27px;
    color: var(--green);
  }
  .slogan-swoosh { position: absolute; left: 300px; top: 172px; }

  .contact {
    position: absolute; left: 56px; top: 222px;
    font-family: "Marcellus SC", serif;
    font-size: 13px; line-height: 18px;
    color: var(--ink-blue);
    list-style: none;
  }
  .contact .rep-label { margin-bottom: 4px; }
  .contact .label { margin-right: 4px; }

  /* Back card */
  .card-back {
    position: absolute; left: 605px; top: 198px;
    width: 515px; height: 288px;
    background: var(--navy);
    overflow: hidden;
  }
  .emblem-field {
    position: absolute; left: 130px; top: 0; right: 0; bottom: 0;
    background: radial-gradient(ellipse at 60% 45%, rgba(47,143,192,0.45) 0%, rgba(47,143,192,0.15) 45%, rgba(43,93,142,0) 75%);
  }
  .services {
    position: absolute; left: 0; top: 122px;
    list-style: none;
    font-family: "Marcellus SC", serif;
    font-size: 13px; line-height: 28px;
    color: var(--light-text);
    letter-spacing: 0.5px;
  }
  .services li { display: flex; align-items: center; }
  .services li::before {
    content: ""; display: block;
    width: 23px; height: 1px;
    background: var(--light-text);
    margin-right: 9px;
  }
  .brand-name--back {
    position: absolute; left: 338px; top: 226px;
    font-family: "Marcellus SC", serif;
    font-size: 16px; line-height: 18px;
    color: var(--paper);
    letter-spacing: 1px;
  }
</style>
</head>
<body>
<main class="canvas">

  <section class="card-front" aria-label="Business card front">
    <div class="edge-stripe edge-stripe--blue"></div>
    <div class="edge-stripe edge-stripe--green"></div>

    <div class="brand-name">Brightmeadow<br>Services</div>

    <p class="slogan">Your Everything<br>Outside Company</p>
    <svg class="slogan-swoosh" width="150" height="26" viewBox="0 0 150 26" aria-hidden="true">
      <path d="M4 22 C 40 8, 100 4, 146 6" fill="none" stroke="var(--green)" stroke-width="2.5" stroke-linecap="round"/>
    </svg>

    <ul class="contact">
      <li class="rep-label">Salemans</li>
      <li><span class="label">Phone:</span> 555-204-3816</li>
      <li><span class="label">Mail:</span> brightmeadowgroup@mailvane.com</li>
    </ul>
  </section>

  <section class="card-back" aria-label="Business card back">
    <div class="emblem-field" role="img" aria-label="Large brand emblem decoration in blue and green tones"></div>
    <ul class="services">
      <li>Lawn Service</li>
      <li>Fertilization</li>
      <li>Pool Service</li>
      <li>Pressure Washing</li>
    </ul>
    <div class="brand-name--back">Brightmeadow<br>Services</div>
  </section>

</main>
</body>
</html>
```